updated documents

Hi i have included a new picture for the about us section, i have also included the updated word document, all changes have been highlighted.

Thanks,

Leon

```html
<!DOCTYPE html>
<html lang="en">
<head>
<meta charset="utf-8">
<title>Keystone Property Services – Business Brochure</title>
<link rel="stylesheet" href="https://fonts.googleapis.com/css2?family=Cinzel:wght@400;600&family=Crimson+Text:wght@400;600&display=swap">
<style>
  :root {
    --lime: #a6c93a;
    --lime-light: #bcd85a;
    --slate: #6a6b6d;
    --slate-dark: #58595b;
    --paper: #ffffff;
    --ink: #2e2e2e;
    --stage: #e9e9ea;
  }
  html, body {
    margin: 0;
    padding: 0;
    overflow: hidden;
    background: var(--stage);
  }
  .spread {
    position: relative;
    width: 1200px;
    height: 847px;
    background: var(--paper);
    overflow: hidden;
  }
  .artwork {
    position: absolute;
    inset: 0;
  }
  .fold-line {
    position: absolute;
    left: 599px;
    top: 0;
    width: 2px;
    height: 847px;
    background: linear-gradient(to right, rgba(0,0,0,0.04), rgba(0,0,0,0));
  }
  .brand {
    position: absolute;
    top: 96px;
    right: 210px;
    display: flex;
    align-items: center;
    gap: 12px;
  }
  .brand-mark {
    width: 18px;
    height: 18px;
    background: var(--lime);
    flex: none;
  }
  .brand-name {
    font-family: "Cinzel", serif;
    font-weight: 600;
    font-size: 20px;
    letter-spacing: 0.5px;
    color: var(--slate-dark);
    white-space: nowrap;
  }
  .title {
    position: absolute;
    left: 795px;
    top: 650px;
    margin: 0;
    font-family: "Cinzel", serif;
    font-weight: 400;
    font-size: 42px;
    line-height: 50px;
    letter-spacing: 1px;
  }
  .title-line { display: block; }
  .title-line--slate { color: var(--slate); }
  .title-line--lime { color: var(--lime); margin-left: 18px; }
  .contact {
    position: absolute;
    left: 46px;
    top: 588px;
  }
  .contact-heading {
    margin: 0 0 12px;
    font-family: "Cinzel", serif;
    font-weight: 600;
    font-size: 22px;
    color: var(--ink);
  }
  .contact-list {
    list-style: none;
    margin: 0;
    padding: 0;
    font-family: "Crimson Text", serif;
    font-size: 17px;
    color: var(--ink);
  }
  .contact-item {
    display: flex;
    align-items: center;
    gap: 8px;
    height: 29px;
  }
  .contact-icon {
    width: 18px;
    height: 18px;
    flex: none;
  }
</style>
</head>
<body>
<main class="spread">
  <svg class="artwork" width="1200" height="847" viewBox="0 0 1200 847">
    <defs>
      <linearGradient id="handshake-tones" x1="0" y1="0" x2="1" y2="1">
        <stop offset="0" stop-color="#cfe0ef"/>
        <stop offset="0.5" stop-color="#9fb8d0"/>
        <stop offset="1" stop-color="#e6eef5"/>
      </linearGradient>
      <linearGradient id="office-tones" x1="0" y1="0" x2="1" y2="1">
        <stop offset="0" stop-color="#c9cdd0"/>
        <stop offset="0.55" stop-color="#8d9397"/>
        <stop offset="1" stop-color="#e2e4e5"/>
      </linearGradient>
      <linearGradient id="lime-sheen" x1="0" y1="1" x2="1" y2="0">
        <stop offset="0" stop-color="var(--lime)"/>
        <stop offset="1" stop-color="var(--lime-light)"/>
      </linearGradient>
    </defs>

    <!-- back page: photo panel and straight diagonal bands -->
    <polygon class="photo photo--handshake" role="img" aria-label="Photo of two business people shaking hands"
             points="0,0 430,0 0,390" fill="url(#handshake-tones)"/>
    <line class="band band--lime" x1="-40" y1="430" x2="480" y2="-40"
          stroke="var(--lime)" stroke-width="72"/>
    <line class="band band--slate" x1="-40" y1="580" x2="220" y2="345"
          stroke="var(--slate)" stroke-width="46"/>

    <!-- cover: crossing straight bands and framed photo -->
    <line class="band band--slate" x1="500" y1="-20" x2="1240" y2="590"
          stroke="var(--slate)" stroke-width="80"/>
    <line class="band band--lime" x1="520" y1="880" x2="1060" y2="180"
          stroke="url(#lime-sheen)" stroke-width="78"/>
    <rect class="photo-frame" x="412" y="232" width="356" height="300" fill="var(--paper)"/>
    <rect class="photo photo--office" role="img" aria-label="Photo of a bright modern office with white desks and computers"
          x="424" y="244" width="332" height="276" fill="url(#office-tones)"/>
  </svg>

  <div class="fold-line"></div>

  <header class="brand">
    <span class="brand-mark"></span>
    <span class="brand-name">Keystone Property Services</span>
  </header>

  <h1 class="title">
    <span class="title-line title-line--slate">Business</span>
    <span class="title-line title-line--lime">Brochure</span>
  </h1>

  <section class="contact">
    <h2 class="contact-heading">Contact Us</h2>
    <ul class="contact-list">
      <li class="contact-item">
        <svg class="contact-icon" viewBox="0 0 18 18" aria-hidden="true">
          <circle cx="9" cy="9" r="8" fill="none" stroke="var(--ink)" stroke-width="1.2"/>
          <path d="M6 5.5c0.5-0.6 1.2-0.6 1.5 0l0.6 1.3c0.2 0.4 0 0.8-0.3 1l-0.5 0.4c0.5 1 1.3 1.8 2.3 2.3l0.4-0.5c0.2-0.3 0.6-0.5 1-0.3l1.3 0.6c0.6 0.3 0.6 1 0 1.5c-0.8 0.8-2 0.9-3.4 0c-1.4-0.9-2.6-2.1-3.4-3.4c-0.6-1.2-0.6-2.3 0.5-2.9z" fill="var(--ink)"/>
        </svg>
        0400 318 256
      </li>
      <li class="contact-item">
        <svg class="contact-icon" viewBox="0 0 18 18" aria-hidden="true">
          <circle cx="9" cy="9" r="8" fill="none" stroke="var(--ink)" stroke-width="1.2"/>
          <rect x="4.5" y="6" width="9" height="6" fill="var(--ink)"/>
          <polyline points="4.5,6 9,9.5 13.5,6" fill="none" stroke="var(--paper)" stroke-width="0.9"/>
        </svg>
        leonv@keystoneps.com.au
      </li>
      <li class="contact-item">
        <svg class="contact-icon" viewBox="0 0 18 18" aria-hidden="true">
          <circle cx="9" cy="9" r="8" fill="none" stroke="var(--ink)" stroke-width="1.2"/>
          <circle cx="9" cy="9" r="4.6" fill="none" stroke="var(--ink)" stroke-width="1"/>
          <ellipse cx="9" cy="9" rx="2" ry="4.6" fill="none" stroke="var(--ink)" stroke-width="0.9"/>
          <line x1="4.4" y1="9" x2="13.6" y2="9" stroke="var(--ink)" stroke-width="0.9"/>
        </svg>
        www.keystonepropertyservices.com
      </li>
      <li class="contact-item">
        <svg class="contact-icon" viewBox="0 0 18 18" aria-hidden="true">
          <circle cx="9" cy="9" r="8" fill="none" stroke="var(--ink)" stroke-width="1.2"/>
        </svg>
        www.social.example/keystoneproperty
      </li>
    </ul>
  </section>
</main>
</body>
</html>
```